vortane realty business card

We need a Business card for our new business. The logo was designed by ArtQuillo, and the text We want on the back is:
REAL ESTATE INVESTMENTS
- BUY, RENOVATE, SELL AND RENT RESIDENTIAL PROPERTIES
- FULL HOME REHABBING , REMODELING AND INTERIOR DESIGN
- HOME STAGING SERVICES
- WHOLESALE INVESTOR PROPERTIES
- MAKE CASH OFFERS ON HOUSES IN ANY CONDITION AND IN ANY SITUATION
- PRIVATE MONEY INVESTOR PROGRAMS WITH 6-12% RETURNS
- PAY CASH REWARDS FOR REFFERALS
- CONCIERGE SERVICE

```html
<!DOCTYPE html>
<html lang="en">
<head>
<meta charset="utf-8">
<title>Vortane Realty business card</title>
<link rel="stylesheet" href="https://fonts.googleapis.com/css2?family=Questrial&family=Source+Sans+3:wght@400;600&display=swap">
<style>
  :root {
    --page: #eef0f1;
    --sky: #5cc3dc;
    --sky-deep: #48b3cf;
    --white: #ffffff;
    --grey: #8d9093;
    --grey-light: #b5b8ba;
    --heading: #8a7d78;
  }
  * { box-sizing: border-box; margin: 0; padding: 0; }
  html, body { width: 1200px; height: 784px; overflow: hidden; }
  body { background: var(--page); position: relative; font-family: "Source Sans 3", sans-serif; }

  .card {
    position: absolute; width: 560px; height: 320px; overflow: hidden;
    box-shadow: 0 6px 18px rgba(0,0,0,.12);
  }
  .card--back { left: 60px; top: 70px; background: linear-gradient(160deg, var(--sky) 0%, var(--sky-deep) 100%); }
  .card--front { left: 600px; top: 400px; background: var(--sky); }

  /* back */
  .services { position: absolute; left: 0; right: 0; top: 34px; text-align: center; font-family: "Questrial", sans-serif; text-transform: uppercase; letter-spacing: .06em; }
  .services__title { color: var(--heading); font-size: 13px; margin-bottom: 10px; }
  .services__list { list-style: none; color: var(--white); font-size: 11.5px; line-height: 21px; }
  .back-brand { position: absolute; right: 26px; bottom: 92px; display: flex; align-items: center; gap: 6px; color: var(--white); font-family: "Questrial", sans-serif; font-size: 13px; letter-spacing: .08em; }
  .back-brand__square { width: 12px; height: 12px; border: 2px solid var(--white); }

  /* front */
  .front-shape { position: absolute; inset: 0; }
  .brand { position: absolute; left: 34px; top: 76px; }
  .brand__name { display: flex; align-items: center; gap: 10px; font-family: "Questrial", sans-serif; font-size: 38px; color: var(--sky); line-height: 1; }
  .brand__square { width: 26px; height: 26px; background: var(--sky); }
  .brand__tagline { margin: 8px 0 0 36px; font-family: "Questrial", sans-serif; font-size: 17px; color: var(--grey); letter-spacing: .06em; }

  .person { position: absolute; right: 238px; top: 220px; text-align: right; }
  .person__name { font-size: 21px; font-weight: 600; color: var(--grey); }
  .person__role { font-size: 11px; color: var(--white); }
  .divider { position: absolute; left: 338px; top: 176px; width: 1px; height: 116px; background: var(--white); }

  .contacts { position: absolute; left: 348px; top: 172px; list-style: none; color: var(--white); font-size: 11.5px; line-height: 15.5px; }
  .contacts li { display: flex; align-items: center; gap: 5px; }
  .contacts svg { width: 10px; height: 10px; flex: none; }
  .contacts .no-icon { padding-left: 15px; }
</style>
</head>
<body>

<section class="card card--back" aria-label="Card back">
  <div class="services">
    <h2 class="services__title">Real Estate Investments</h2>
    <ul class="services__list">
      <li>Buy, renovate, sell and rent residential properties</li>
      <li>Full home rehabbing , remodeling and interior design</li>
      <li>Home staging services</li>
      <li>Wholesale investor properties</li>
      <li>Make cash offers on houses in any condition and in any situation</li>
      <li>Private money investor programs with 6-12% returns</li>
      <li>Pay cash rewards for refferals</li>
      <li>Concierge service</li>
    </ul>
  </div>
  <div class="back-brand"><span class="back-brand__square"></span>VORTANE</div>
</section>

<section class="card card--front" aria-label="Card front">
  <svg class="front-shape" viewBox="0 0 560 320" preserveAspectRatio="none" aria-hidden="true">
    <path d="M0 0 H560 V28 C480 120 330 175 0 300 Z" fill="var(--white)"/>
    <path d="M240 168 C390 125 490 70 536 0 H556 C510 85 400 140 240 168 Z" fill="var(--grey-light)"/>
  </svg>

  <div class="brand">
    <div class="brand__name"><span class="brand__square"></span>VORTANE Realty</div>
    <div class="brand__tagline">REAL ESTATE SOLUTIONS</div>
  </div>

  <div class="person">
    <div class="person__name">Marcus Hale</div>
    <div class="person__role">Executive Director</div>
  </div>

  <div class="divider"></div>

  <ul class="contacts">
    <li><svg viewBox="0 0 10 10"><rect x="2.5" y="0.5" width="5" height="9" rx="1" fill="none" stroke="#fff"/></svg>555-214-3380</li>
    <li><svg viewBox="0 0 10 10"><path d="M2 1 L4 1 L4.5 3 L3.3 4 Q4.5 6 6 6.7 L7 5.5 L9 6 L9 8 Q5 9 1 3 Z" fill="#fff"/></svg>555-214-6092</li>
    <li><svg viewBox="0 0 10 10"><rect x="1" y="2" width="8" height="6" rx="1" fill="#fff"/></svg>555-214-7715</li>
    <li><svg viewBox="0 0 10 10"><rect x="0.5" y="2" width="9" height="6" fill="none" stroke="#fff"/><path d="M0.5 2 L5 5.5 L9.5 2" fill="none" stroke="#fff"/></svg>marcus@vortanerealty.com</li>
    <li><svg viewBox="0 0 10 10"><circle cx="5" cy="5" r="4.2" fill="none" stroke="#fff"/><path d="M1 5 H9 M5 1 V9" stroke="#fff" stroke-width=".8"/></svg>www.vortanerealty.com</li>
    <li><svg viewBox="0 0 10 10"><path d="M5 1 L9.5 5 H8 V9 H2 V5 H0.5 Z" fill="#fff"/></svg>418 Elm Row</li>
    <li class="no-icon">PO Box 356 Fairhaven, NC 27990</li>
  </ul>
</section>

</body>
</html>
```